We sell companies excess stock for them

We need a business card for a company based in New Zealand called 'StockHarbor'.

Check out our website to get an idea www.stockharbor.example

We help other businesses to;
- Sell Excess Stock
- Manage Product Returns
- Sell Company Assets

Our logo is attached for your reference
The font used is 'RifficFree-Bold'

Target Market(s)

Businesses

Industry/Entity Type

Business

Contact Information for Business Card

Name: Mark Pellow
Phone: 027 846 2093
email: markpellow@stockharbor.example
website: www.stockharbor.example

Font styles to use
Other font styles liked:
• Unsure

Colors
9bcb3b

Requirements
Must have
• coming soon
Nice to have
• coming soon
Should not have
• coming soon

```html
<!DOCTYPE html>
<html lang="en">
<head>
<meta charset="utf-8">
<title>StockHarbor Business Card</title>
<link rel="stylesheet" href="https://fonts.googleapis.com/css2?family=Fredoka:wght@700&family=Montserrat:wght@400;500&display=swap">
<style>
  :root {
    --green: #8cc63f;
    --green-dark: #1a9b3c;
    --ink: #2e2b28;
    --text: #3a3a3a;
    --paper: #ffffff;
    --backdrop: #e9e7e4;
    --mascot-tone: #e9a23b;
  }
  html, body {
    margin: 0;
    width: 1200px;
    height: 797px;
    overflow: hidden;
    background: var(--backdrop);
  }
  .stage {
    position: relative;
    width: 1200px;
    height: 797px;
  }
  .card {
    position: absolute;
    top: 255px;
    width: 500px;
    height: 286px;
    background: var(--paper);
    box-shadow: 0 6px 18px rgba(0,0,0,0.18);
    overflow: hidden;
  }
  .card-front { left: 70px; }
  .card-back { left: 630px; }

  .brand-name {
    position: absolute;
    inset: 0;
    display: flex;
    align-items: center;
    justify-content: center;
    font-family: "Fredoka", sans-serif;
    font-weight: 700;
    font-size: 54px;
    letter-spacing: -1px;
    color: var(--ink);
  }

  .stripe {
    position: absolute;
    height: 5px;
    background: var(--green);
    top: 170px;
  }
  .stripe-left { left: 0; width: 78px; }
  .stripe-right { left: 200px; right: 0; }

  .mascot {
    position: absolute;
    left: 92px;
    top: 112px;
    width: 100px;
    height: 108px;
    border-radius: 12px;
    background: linear-gradient(135deg, var(--mascot-tone), var(--green));
  }

  .identity {
    position: absolute;
    left: 210px;
    top: 118px;
  }
  .person-name {
    font-family: "Montserrat", sans-serif;
    font-weight: 500;
    font-size: 15px;
    color: var(--green);
    margin: 0;
    letter-spacing: 0.3px;
  }
  .person-role {
    display: inline-block;
    margin-top: 2px;
    padding: 1px 40px 1px 4px;
    background: var(--green-dark);
    color: #fff;
    font-family: "Montserrat", sans-serif;
    font-size: 11px;
    font-weight: 500;
  }

  .contacts {
    position: absolute;
    left: 222px;
    top: 186px;
    margin: 0;
    padding: 0;
    list-style: none;
    font-family: "Montserrat", sans-serif;
    font-size: 11px;
    color: var(--text);
    line-height: 16px;
  }
  .contacts li {
    display: flex;
    align-items: flex-start;
    gap: 8px;
  }
  .contacts svg {
    width: 10px;
    height: 10px;
    margin-top: 3px;
    flex: none;
    stroke: var(--green);
    fill: none;
    stroke-width: 1.4;
  }
</style>
</head>
<body>
<main class="stage">
  <section class="card card-front">
    <div class="brand-name">StockHarbor</div>
  </section>

  <section class="card card-back">
    <div class="stripe stripe-left"></div>
    <div class="stripe stripe-right"></div>

    <div class="mascot" role="img" aria-label="Cartoon delivery mascot carrying a box, giving a thumbs up"></div>

    <div class="identity">
      <p class="person-name">JOHN SMITH</p>
      <span class="person-role">Manager</span>
    </div>

    <ul class="contacts">
      <li>
        <svg viewBox="0 0 10 10"><rect x="2.5" y="0.8" width="5" height="8.4" rx="1"/></svg>
        <span>123 456 7890</span>
      </li>
      <li>
        <svg viewBox="0 0 10 10"><rect x="0.8" y="2" width="8.4" height="6"/><path d="M0.8 2 L5 5.5 L9.2 2"/></svg>
        <span>info@website.com</span>
      </li>
      <li>
        <svg viewBox="0 0 10 10"><rect x="0.8" y="1.2" width="8.4" height="5.6"/><path d="M3 9 H7"/></svg>
        <span>www.website.com</span>
      </li>
      <li>
        <svg viewBox="0 0 10 10"><path d="M5 9.2 C2 6 1.8 4.8 1.8 3.8 A3.2 3.2 0 0 1 8.2 3.8 C8.2 4.8 8 6 5 9.2 Z"/><circle cx="5" cy="3.8" r="1"/></svg>
        <span>Address Line 1<br>Address Line 2</span>
      </li>
    </ul>
  </section>
</main>
</body>
</html>
```